Home Care company needs letter head branding

Home care company needs a letter head which can be used for all documents the company's clients view. We provided in home care for the elderly. We would like to use our company colors (2785A7, 0A4057 and 34A74D) and should not be too large as we will be using it on more than just a letter head but all documents our clients sign / receive.
Target Market(s)
Professional business
Industry/Entity Type
Health Care
Requirements
Must have
- corporate brand colors

```html
<!DOCTYPE html>
<html lang="en">
<head>
<meta charset="utf-8">
<title>Maplebrook Care Letterhead</title>
<link href="https://fonts.googleapis.com/css2?family=Roboto:wght@500;700&display=swap" rel="stylesheet">
<style>
  :root {
    --backdrop: #bdbdbf;
    --paper: #f6f6f6;
    --brand-blue: #2785a7;
    --brand-deep: #0a4057;
    --charcoal: #3b3b3c;
    --ink: #2b2b2b;
    --mark-tint: #dbe7ec;
  }
  html, body {
    margin: 0;
    padding: 0;
    width: 1200px;
    height: 1200px;
    overflow: hidden;
    background: var(--backdrop);
    font-family: "Roboto", Arial, sans-serif;
  }
  .letterhead {
    position: absolute;
    left: 175px;
    top: 50px;
    width: 850px;
    height: 1100px;
    background: var(--paper);
    box-shadow: 0 4px 14px rgba(0,0,0,0.18);
  }
  .brand {
    position: absolute;
    left: 74px;
    top: 64px;
    display: flex;
    align-items: center;
    gap: 10px;
  }
  .brand-dot {
    width: 58px;
    height: 58px;
    border-radius: 50%;
    background: var(--brand-blue);
  }
  .brand-name {
    font-weight: 500;
    font-size: 29px;
    color: var(--brand-blue);
    letter-spacing: -0.2px;
  }
  .contact {
    position: absolute;
    left: 625px;
    top: 44px;
    font-weight: 700;
    font-size: 14px;
    line-height: 17px;
    color: var(--ink);
  }
  .contact-row {
    display: flex;
    align-items: flex-start;
    gap: 8px;
    margin-bottom: 4px;
  }
  .contact-row svg { flex: none; margin-top: 2px; }
  .backdrop-mark {
    position: absolute;
    left: 307px;
    top: 428px;
    width: 236px;
    height: 236px;
    border-radius: 50%;
    background: var(--mark-tint);
    opacity: 0.6;
  }
  .footer {
    position: absolute;
    left: 0;
    bottom: 0;
    width: 850px;
    height: 48px;
  }
  .footer-web {
    position: absolute;
    right: 60px;
    bottom: 14px;
    color: #ffffff;
    font-weight: 500;
    font-size: 16px;
  }
</style>
</head>
<body>
  <main class="letterhead">
    <header class="brand">
      <span class="brand-dot"></span>
      <span class="brand-name">Maplebrook Care</span>
    </header>

    <address class="contact" style="font-style:normal">
      <div class="contact-row">
        <svg width="12" height="14" viewBox="0 0 12 14"><path d="M6 0a5 5 0 0 0-5 5c0 3.6 5 9 5 9s5-5.4 5-9a5 5 0 0 0-5-5zm0 7a2 2 0 1 1 0-4 2 2 0 0 1 0 4z" fill="var(--brand-blue)"/></svg>
        <span>2364 First Address Line<br>Second Address Line</span>
      </div>
      <div class="contact-row">
        <svg width="12" height="12" viewBox="0 0 12 12"><path d="M2.5 0.5l2 2.4-1.2 1.5c.8 1.7 2 2.9 3.7 3.8l1.5-1.2 2.4 2-1.2 2.2C4.8 10.8 1 7 .3 1.7z" fill="var(--brand-blue)"/></svg>
        <span>+ 0 123 456 7899</span>
      </div>
      <div class="contact-row">
        <svg width="12" height="12" viewBox="0 0 12 12"><rect x="0.7" y="2" width="10.6" height="8" fill="none" stroke="var(--brand-blue)" stroke-width="1.4"/><path d="M1 2.5l5 4 5-4" fill="none" stroke="var(--brand-blue)" stroke-width="1.4"/></svg>
        <span>lorem@ipsum.com</span>
      </div>
    </address>

    <div class="backdrop-mark" role="img" aria-label="Faint brand mark area"></div>

    <footer class="footer">
      <svg width="850" height="48" viewBox="0 0 850 48">
        <path d="M0 22 H556 L548 31 H0 Z" fill="var(--brand-blue)"/>
        <rect x="0" y="39" width="850" height="9" fill="var(--charcoal)"/>
        <path d="M548 48 L570 22 C590 4 610 0 630 0 H850 V48 Z" fill="var(--charcoal)"/>
      </svg>
      <span class="footer-web">websitename.com</span>
    </footer>
  </main>
</body>
</html>
```